WHERE RIVERS LEARN TO SING

Where Rivers Learn To Sing is the title of my book. The book is written to specifically address a major issue the world over which is the ability of think. Educational system in many parts of the world trains us to DO as supposed to Create. In the new world order, doing will always be inferior to thinking. The book is packed with methodologies and case studies. I need a unique design for the book.
Visual of the human brain as part of the creative element / rendition
Since the book is about creative thinking and innovation, I need a creative masterpiece that will be appealing to the eye on the shelf with a strong connection of curiosity & engagement. I personally am of the opinion that visual of the brain is quite off putting
AUTHOR: TUNDE OKORAFOR
PRINTED BY: MERIDIAN LEAF BOOKS
BOOK SIZE: A5

Target Market(s)

Middle to Senior Level Managers in the Private Sector, Fresh Graduates, Entrepreneurs & SME Owners, Government

Font styles to use
Serif

Colors

Designer to choose colors to be used in the design.

Requirements
Must have
• On the front cover, in addition to the title, it should also have the pay off ''Discover & Discover & Unleash The Power Of Your Creative Mind
• Simple back cover design that allows for authors note etc to be very legible
• another must have is space for authors picture
• Front cover Star Burst (WARNING: this book will be difficult to lend)
Should not have
• Visual of the human brain as part of the creative element / rendition

```html
<!DOCTYPE html>
<html lang="en">
<head>
<meta charset="utf-8">
<title>Where Rivers Learn To Sing — Cover Spread</title>
<link rel="stylesheet" href="https://fonts.googleapis.com/css2?family=Jost:ital,wght@0,500;0,700;0,800;1,300;1,700&family=Noto+Sans:wght@400&display=swap">
<style>
  :root {
    --stage: #000000;
    --blue-deep: #0b5fb4;
    --blue-mid: #0b8ad3;
    --blue-bright: #19a6e6;
    --glow: rgba(190, 230, 255, 0.55);
    --ink-light: #ffffff;
    --placeholder-ink: #b8bcc0;
    --hand-tone: #d2ab93;
  }
  * { box-sizing: border-box; margin: 0; padding: 0; }
  html, body {
    width: 1200px; height: 1200px; overflow: hidden;
    background: var(--stage);
  }
  .spread {
    position: absolute; left: 33px; top: 172px;
    width: 1134px; height: 856px; overflow: hidden;
    background:
      radial-gradient(ellipse 520px 60px at 560px 470px, var(--glow), transparent 70%),
      radial-gradient(ellipse 300px 220px at 860px 500px, rgba(200,235,255,0.45), transparent 70%),
      radial-gradient(ellipse 700px 420px at 300px 420px, rgba(60,170,235,0.5), transparent 75%),
      radial-gradient(ellipse 420px 500px at 1134px 700px, var(--blue-deep), transparent 80%),
      linear-gradient(180deg, var(--blue-mid) 0%, var(--blue-bright) 55%, var(--blue-mid) 100%);
    font-family: "Jost", sans-serif;
    color: var(--ink-light);
  }
  .title {
    position: absolute; text-align: center; text-transform: uppercase;
    font-weight: 700; letter-spacing: -0.02em; line-height: 1;
    text-shadow: 0 2px 3px rgba(0, 40, 90, 0.35);
  }
  .title span { position: absolute; left: 0; right: 0; white-space: nowrap; }

  .back-title { left: 47px; top: 0; width: 284px; height: 320px; }
  .back-title .l1 { top: 109px; font-size: 46px; }
  .back-title .l2 { top: 156px; font-size: 31px; }
  .back-title .l3 { top: 188px; font-size: 57px; }
  .back-title .l4 { top: 232px; font-size: 80px; }

  .front-title { left: 667px; top: 0; width: 376px; height: 370px; }
  .front-title .l1 { top: 32px; font-size: 80px; }
  .front-title .l2 { top: 111px; font-size: 54px; }
  .front-title .l3 { top: 166px; font-size: 96px; }
  .front-title .l4 { top: 240px; font-size: 137px; }

  .author {
    position: absolute; font-weight: 700; text-transform: uppercase;
    white-space: nowrap; text-align: center;
    text-shadow: 0 1px 2px rgba(0, 40, 90, 0.3);
  }
  .back-author { left: 53px; width: 276px; top: 323px; font-size: 24px; letter-spacing: 0.18em; }
  .front-author { left: 631px; width: 452px; top: 758px; font-size: 40px; line-height: 56px; letter-spacing: 0.15em; }

  .author-photo {
    position: absolute; left: 357px; top: 185px; width: 141px; height: 164px;
    background: var(--ink-light);
    display: flex; align-items: center; justify-content: center; text-align: center;
    font-family: "Noto Sans", sans-serif; font-size: 20px; line-height: 1.05;
    color: var(--placeholder-ink);
  }
  .spine-text {
    position: absolute; left: 552px; top: 120px; width: 30px; height: 580px;
    writing-mode: vertical-rl; font-weight: 700; font-size: 22px;
    letter-spacing: -0.01em; line-height: 30px; white-space: nowrap;
    text-transform: uppercase; text-shadow: 0 1px 2px rgba(0, 40, 90, 0.3);
  }
  .spine-text .gap { display: inline-block; height: 18px; }
  .publisher {
    position: absolute; left: 10px; top: 782px; width: 200px; text-align: center;
    font-family: "Noto Sans", sans-serif; font-size: 17px; line-height: 1.1;
  }
  .tagline {
    position: absolute; left: 647px; top: 374px; width: 416px; text-align: center;
    font-style: italic; text-transform: uppercase; line-height: 26px;
  }
  .tagline .lead { font-weight: 300; font-size: 19px; }
  .tagline .payoff { font-weight: 700; font-size: 19px; }
  .hero-photo {
    position: absolute; left: 811px; top: 456px; width: 323px; height: 400px;
  }
</style>
</head>
<body>
  <main class="spread">
    <section class="back-cover">
      <h2 class="title back-title">
        <span class="l1">Where</span>
        <span class="l2">Rivers Learn</span>
        <span class="l3">To</span>
        <span class="l4">Sing</span>
      </h2>
      <p class="author back-author">Tunde Okorafor</p>
      <div class="author-photo">TUNDE<br>OKORAFOR’s<br>PHOTO</div>
      <p class="publisher">MERIDIAN LEAF BOOKS<br>Logo</p>
    </section>

    <section class="spine">
      <p class="spine-text">Where Rivers Learn To Sing<span class="gap"></span>Tunde Okorafor</p>
    </section>

    <section class="front-cover">
      <svg class="hero-photo" role="img" aria-label="Photo of a hand holding up a glowing white light bulb" viewBox="0 0 323 400">
        <defs>
          <radialGradient id="bulbGlow" cx="0.4" cy="0.2" r="0.35">
            <stop offset="0" stop-color="#ffffff" stop-opacity="0.95"/>
            <stop offset="0.5" stop-color="#ffffff" stop-opacity="0.5"/>
            <stop offset="1" stop-color="#ffffff" stop-opacity="0"/>
          </radialGradient>
          <radialGradient id="handTone" cx="0.6" cy="0.85" r="0.55">
            <stop offset="0" stop-color="var(--hand-tone)" stop-opacity="0.55"/>
            <stop offset="1" stop-color="var(--hand-tone)" stop-opacity="0"/>
          </radialGradient>
        </defs>
        <rect width="323" height="400" fill="url(#handTone)"/>
        <rect width="323" height="400" fill="url(#bulbGlow)"/>
      </svg>
      <h1 class="title front-title">
        <span class="l1">Where</span>
        <span class="l2">Rivers Learn</span>
        <span class="l3">To</span>
        <span class="l4">Sing</span>
      </h1>
      <p class="tagline">
        <span class="lead">It should also have the pay off</span><br>
        <span class="payoff">Discover &amp; Unleash the power of<br>your creative mind</span>
      </p>
      <p class="author front-author">Tunde Okorafor</p>
    </section>
  </main>
</body>
</html>
```